Nature and Scenic Photographs Business Card Design

I require a simple business card using the illustration that I have provided

Industry/Entity Type

Business

Contact Information for Business Card

Gil Harlow
Mobile: 0436182057
Skype: gilbert.moray.harlow

```html
<!DOCTYPE html>
<html lang="en">
<head>
<meta charset="utf-8">
<title>Gil Harlow — Business Card</title>
<link rel="stylesheet" href="https://fonts.googleapis.com/css2?family=Jost:wght@400;600&display=swap">
<style>
  :root {
    --page-bg: #161616;
    --card-light: #f4f4f4;
    --card-mid: #e2e2e3;
    --card-edge: #d2d3d5;
    --ink: #111111;
    --forest-dark: #2c3a1c;
    --forest-mid: #5d6b30;
    --forest-light: #8f9a4c;
  }
  * { margin: 0; padding: 0; box-sizing: border-box; }
  html, body {
    width: 1200px;
    height: 1200px;
    overflow: hidden;
    background: var(--page-bg);
  }
  .canvas {
    position: relative;
    width: 1200px;
    height: 1200px;
  }
  .card {
    position: absolute;
    left: 50px;
    top: 261px;
    width: 1100px;
    height: 678px;
    background: radial-gradient(ellipse at 72% 45%, var(--card-light) 0%, var(--card-mid) 60%, var(--card-edge) 100%);
    font-family: "Jost", "Futura", sans-serif;
    color: var(--ink);
  }
  .card__photo {
    position: absolute;
    left: 0;
    top: 174px;
    width: 582px;
    height: 354px;
    background:
      radial-gradient(ellipse at 30% 75%, var(--forest-mid) 0%, transparent 55%),
      radial-gradient(ellipse at 80% 25%, var(--forest-light) 0%, transparent 45%),
      linear-gradient(180deg, var(--forest-mid) 0%, var(--forest-dark) 100%);
  }
  .card__frame {
    position: absolute;
    left: 670px;
    top: 194px;
    width: 354px;
    height: 144px;
  }
  .card__name {
    position: absolute;
    right: 78px;
    top: 382px;
    font-size: 50px;
    line-height: 1;
    letter-spacing: 3px;
    font-weight: 400;
    white-space: nowrap;
  }
  .card__name strong { font-weight: 600; }
  .card__contact {
    position: absolute;
    right: 86px;
    top: 474px;
    text-align: right;
    font-size: 20px;
    line-height: 30px;
    letter-spacing: 1px;
  }
</style>
</head>
<body>
  <div class="canvas">
    <section class="card">
      <div class="card__photo" role="img" aria-label="Photograph of a mossy rainforest floor with fallen branches and ferns"></div>
      <svg class="card__frame" viewBox="0 0 354 144" aria-hidden="true">
        <g fill="none" stroke="#111" stroke-width="4">
          <polyline points="2,42 2,2 40,2"/>
          <polyline points="314,2 352,2 352,42"/>
          <polyline points="2,102 2,142 40,142"/>
          <polyline points="314,142 352,142 352,102"/>
        </g>
      </svg>
      <h1 class="card__name">GIL <strong>HARLOW</strong></h1>
      <p class="card__contact">
        Mobile: 0436182057<br>
        Skype: gilbert.moray.harlow
      </p>
    </section>
  </div>
</body>
</html>
```